Business card for Drone Aerial

I need a business card designed keeping in mind I want to do post cards also with a similar design.
Both sides of the card would be cool.
I have a skylark 5 max and would like a picture of it on the front of the card. Similar to one I attached.
I really like the look of a drone in the air and the background pic a little blurry. I attached a few images as IDEAS.
Some special things I want to be on the card additional to the normal business card info:
"Aerial Photography" or "Low Altitude Aerial Photography"?
"ZQB# 90817263"

I like modern and creative. My Favorite color is blue and I like blue on white.
I do not have a business name and am not going to have one. When they read "Aerial Photography" and see the drone and image they will know what the card is for.

FYI, The attached pictures are just images from framewillow and just samples/ideas.

Target Market(s)

Real estate, construction, events

Industry/Entity Type

Business

Contact Information for Business Card

Also Definitely want to contain, my name, my number and email address.

Requirements
Must have
• "ZQB# 90817263"
• "Aerial Photography"

```html
<!DOCTYPE html>
<html lang="en">
<head>
<meta charset="utf-8">
<title>Aerial Photography – Business Card</title>
<link href="https://fonts.googleapis.com/css2?family=Exo+2:wght@700;800&family=Open+Sans:wght@400;700&display=swap" rel="stylesheet">
<style>
  :root {
    --page-bg: #e4e5e8;
    --sky-top: #0c1646;
    --sky-mid: #2238a4;
    --sky-glow: #3c5fd2;
    --drone-glow: rgba(170,190,235,0.55);
    --city-glow: rgba(60,150,210,0.55);
    --city-dark: #08142e;
    --panel-blue: #3a47a8;
    --panel-deep: #323f9c;
    --title-pale: #bccbe8;
    --white: #ffffff;
  }
  * { margin: 0; padding: 0; box-sizing: border-box; }
  html, body { width: 1200px; height: 1119px; overflow: hidden; background: var(--page-bg); }
  .stage { position: relative; width: 1200px; height: 1119px; }

  .card { position: absolute; width: 692px; height: 396px; overflow: hidden; }
  .card--front { left: 349px; top: 121px; }
  .card--back { left: 200px; top: 600px; }

  .sky-photo {
    position: absolute;
    background:
      radial-gradient(ellipse 24% 30% at 68% 50%, var(--drone-glow), transparent 75%),
      radial-gradient(ellipse 70% 22% at 40% 88%, var(--city-glow), transparent 80%),
      linear-gradient(180deg, var(--sky-top) 0%, var(--sky-mid) 45%, var(--sky-glow) 66%, #1d3a86 80%, var(--city-dark) 100%);
  }
  .card--front .sky-photo { inset: 0; }
  .card--back .sky-photo {
    left: 342px; top: 0; right: 0; bottom: 0;
    background:
      radial-gradient(ellipse 45% 34% at 50% 50%, var(--drone-glow), transparent 75%),
      radial-gradient(ellipse 90% 20% at 40% 92%, var(--city-glow), transparent 80%),
      linear-gradient(180deg, var(--sky-top) 0%, var(--sky-mid) 45%, var(--sky-glow) 68%, #1d3a86 82%, var(--city-dark) 100%);
  }

  .brand-title { position: absolute; font-family: "Exo 2", sans-serif; line-height: 1; }
  .brand-title__main { display: block; font-weight: 800; letter-spacing: 1px; }
  .brand-title__sub { display: block; font-weight: 700; letter-spacing: 1.5px; }

  .card--front .brand-title { left: 14px; top: 26px; color: var(--title-pale); text-align: center; width: 310px; }
  .card--front .brand-title__main { font-size: 76px; }
  .card--front .brand-title__sub { font-size: 36px; margin-top: -4px; }

  .contact-panel {
    position: absolute; left: 0; top: 0; width: 342px; height: 100%;
    background:
      radial-gradient(ellipse 80% 30% at 50% 90%, rgba(30,40,120,0.45), transparent 80%),
      linear-gradient(180deg, var(--panel-blue) 0%, var(--panel-blue) 65%, var(--panel-deep) 100%);
    color: var(--white);
    font-family: "Open Sans", sans-serif;
  }
  .holder { position: absolute; left: 32px; top: 24px; }
  .holder__name { font-size: 27px; font-weight: 700; line-height: 1.1; font-family: "Exo 2", sans-serif; letter-spacing: 0.3px; }
  .holder__licence { font-size: 15.5px; margin-top: 1px; }

  .contact-panel .brand-title { left: 0; width: 342px; top: 104px; text-align: center; color: var(--white); }
  .contact-panel .brand-title__main { font-size: 78px; }
  .contact-panel .brand-title__sub { font-size: 36px; margin-top: -4px; }

  .address { position: absolute; left: 32px; top: 242px; font-size: 16px; line-height: 22px; }
  .contact-list { position: absolute; left: 32px; top: 302px; list-style: none; font-size: 16px; line-height: 22px; }
  .contact-list li { display: flex; align-items: center; gap: 9px; }
  .contact-list svg { width: 16px; height: 16px; flex: none; }
</style>
</head>
<body>
<main class="stage">

  <section class="card card--front" aria-label="Card front">
    <div class="sky-photo" role="img" aria-label="Quadcopter drone hovering over a night city skyline under a starry blue sky"></div>
    <h1 class="brand-title">
      <span class="brand-title__main">Aerial</span>
      <span class="brand-title__sub">PHOTOGRAPHY</span>
    </h1>
  </section>

  <section class="card card--back" aria-label="Card back">
    <div class="contact-panel" role="img" aria-label="Faint blue city skyline behind the contact details">
      <div class="holder">
        <p class="holder__name">Rowan Adair</p>
        <p class="holder__licence">ZQB# 90817263</p>
      </div>
      <h2 class="brand-title">
        <span class="brand-title__main">Aerial</span>
        <span class="brand-title__sub">PHOTOGRAPHY</span>
      </h2>
      <p class="address">#4870, Birch Lane<br>Cedar Falls, Canada</p>
      <ul class="contact-list">
        <li>
          <svg viewBox="0 0 16 16" aria-hidden="true"><circle cx="8" cy="8" r="8" fill="#fff"/><path d="M5.2 4.2l1.6 0 .6 2-1 .8a6 6 0 0 0 2.6 2.6l.8-1 2 .6v1.6c-4 .4-7-2.6-6.6-6.6z" fill="#3a47a8"/></svg>
          <span>412.555.0187</span>
        </li>
        <li>
          <svg viewBox="0 0 16 16" aria-hidden="true"><circle cx="8" cy="8" r="8" fill="#fff"/><rect x="5.3" y="3.5" width="5.4" height="9" rx="1" fill="#3a47a8"/><rect x="6.3" y="4.6" width="3.4" height="5.8" fill="#fff"/></svg>
          <span>412.555.0243</span>
        </li>
        <li>
          <svg viewBox="0 0 16 16" aria-hidden="true"><circle cx="8" cy="8" r="8" fill="#fff"/><rect x="3.8" y="5" width="8.4" height="6" fill="#3a47a8"/><path d="M3.8 5l4.2 3.4L12.2 5" fill="none" stroke="#fff" stroke-width="0.9"/></svg>
          <span>hello@RowanAdairAerial.com</span>
        </li>
      </ul>
    </div>
    <div class="sky-photo" role="img" aria-label="Quadcopter drone flying above a lit city skyline at night"></div>
  </section>

</main>
</body>
</html>
```